Business Card Redesign

We would like to redesign our existing business cards.
The new design shall look:
ELEGANT, LUXURY, PROFESSIONAL
Reference:
YOU CAN VISIT WWW.LUMEN-BRIDGE-PARTNERS.EXAMPLE FOR BETTER UNDERSTANDING OF COMPANY STRATEGY AND POSITION
Additional:
CHOSEN CANDIDATE SHALL PROVIDE THE INSTRUCTION OF PRINTING IF ANY THERMAL COVERAGE OR ANY ADDITION IS OFFERED
Industry/Entity Type
Business

```html
<!DOCTYPE html>
<html lang="en">
<head>
<meta charset="utf-8">
<title>Lumen Bridge Partners – Business Cards</title>
<link rel="stylesheet" href="https://fonts.googleapis.com/css2?family=Open+Sans:wght@400;600;700&family=Noto+Sans+TC:wght@400;700&display=swap">
<style>
  :root {
    --bg: #e4e2de;
    --card: #f3f2ef;
    --brown: #5b3c1f;
    --navy: #1f3b7a;
    --text: #5a5650;
    --rule: #2c4c8f;
  }
  * { margin: 0; padding: 0; box-sizing: border-box; }
  html, body { width: 1200px; height: 900px; overflow: hidden; }
  body {
    background: var(--bg);
    font-family: "Open Sans", sans-serif;
    color: var(--text);
    position: relative;
  }
  .card {
    position: absolute;
    left: 250px;
    width: 700px;
    height: 400px;
    background: var(--card);
    box-shadow: 0 6px 18px rgba(0,0,0,0.15);
    overflow: hidden;
  }
  .card--english { top: 40px; }
  .card--chinese { top: 460px; font-family: "Noto Sans TC", sans-serif; }

  .brand-band {
    position: absolute;
    left: 95px; top: 0;
    width: 110px; height: 285px;
    background: var(--brown);
  }
  .brand-mark {
    position: absolute;
    left: 50%; top: 85px;
    transform: translateX(-50%);
    width: 86px; height: 86px;
    border-radius: 50%;
    background: var(--navy);
  }
  .brand-name {
    position: absolute;
    left: 6px; right: 6px; top: 184px;
    text-align: center;
    color: #ffffff;
    font-family: "Open Sans", sans-serif;
    font-weight: 600;
    font-size: 11px;
    line-height: 1.35;
    letter-spacing: 0.5px;
  }
  .web-address {
    position: absolute;
    left: 28px; top: 308px;
    color: var(--navy);
    font-family: "Open Sans", sans-serif;
    font-size: 13px;
  }
  .foot-block {
    position: absolute;
    left: 105px; top: 340px;
    width: 100px; height: 32px;
    background: var(--brown);
  }

  .details {
    position: absolute;
    left: 290px; top: 44px; right: 0;
    font-size: 13px;
    line-height: 1.5;
  }
  .company { font-size: 13px; letter-spacing: 0.5px; }
  .person {
    color: var(--brown);
    font-weight: 700;
    font-size: 24px;
    line-height: 1.15;
    margin-top: 2px;
  }
  .card--chinese .person { font-size: 22px; }
  .role { font-size: 13px; }
  .divider {
    height: 0;
    border-top: 1.5px solid var(--rule);
    margin: 14px 0 14px 0;
  }
  .office { margin-bottom: 12px; }
  .contact-line span { display: inline-block; width: 16px; }
</style>
</head>
<body>

<section class="card card--english" aria-label="Business card, English side">
  <div class="brand-band">
    <div class="brand-mark"></div>
    <div class="brand-name">LUMEN BRIDGE PARTNERS</div>
  </div>
  <div class="web-address">www.lumen-bridge-partners.example</div>
  <div class="foot-block"></div>

  <div class="details">
    <p class="company">LUMEN BRIDGE PARTNERS LIMITED</p>
    <p class="person">NORA VAIL</p>
    <p class="role">PR Consultant</p>
    <p class="contact-line"><span>E</span>nora@lumen-bridge-partners.example</p>
    <p class="contact-line"><span>M</span>(852) 5550 0142</p>
    <div class="divider"></div>
    <p class="office">HEADQUARTERS (HONG KONG)</p>
    <p>Rm. 808, 8/F, Harbourlight Centre,<br>18 Lantern Street, Central,<br>Hong Kong</p>
    <p class="contact-line" style="margin-top:10px"><span>T</span>(852) 5550 0100</p>
    <p class="contact-line"><span>F</span>(852) 5550 0101</p>
  </div>
</section>

<section class="card card--chinese" lang="zh-Hant" aria-label="Business card, Chinese side">
  <div class="brand-band">
    <div class="brand-mark"></div>
    <div class="brand-name">LUMEN BRIDGE PARTNERS</div>
  </div>
  <div class="web-address">www.lumen-bridge-partners.example</div>
  <div class="foot-block"></div>

  <div class="details">
    <p class="company">明橋顧問有限公司</p>
    <p class="person">林雅文</p>
    <p class="role">公關顧問</p>
    <p>電郵　nora@lumen-bridge-partners.example</p>
    <p>手提　(852) 5550 0142</p>
    <div class="divider"></div>
    <p class="office">香港總部</p>
    <p>香港中環燈籠街18號<br>港光中心8樓808室</p>
    <p style="margin-top:10px">電話　(852) 5550 0100</p>
    <p>傳真　(852) 5550 0101</p>
  </div>
</section>

</body>
</html>
```